All-natural soap packaging design for new company

The box type has been selected, we just need artwork for each of our 10 products. I'd like the same look to each, the idea is just to switch out the name and ingredient label on each. The dimensions are 3.5"x3.75"x1.25". The colors in the uploaded pictures with product titles are not mandatory. I'd like to keep the font on the packaging (Rubik) as it is the same as the website.

Target Market(s)

Health & Beauty, people looking for natural or organic products

Industry/Entity Type

It Company

Colors

Designer to choose colors to be used in the design.

Requirements
Must have
• Design must be clean and relatively simple. Slightly different look for each of the 10 products. Audience is people looking for all-natural products.

```html
<!DOCTYPE html>
<html lang="en">
<head>
<meta charset="UTF-8">
<title>Harlow Soap Co. — Recipe No. 6 Lid Artwork</title>
<link rel="stylesheet" href="https://fonts.googleapis.com/css2?family=Rubik:wght@300;400;500&family=Oswald:wght@300;400&display=swap">
<style>
  :root {
    --backdrop: #d3e2e8;
    --paper: #f7f7f8;
    --violet: #4b2e99;
    --violet-deep: #3a2380;
    --lavender-light: #c9bfe6;
    --lavender-mid: #9d8bd3;
    --stem-grey: #8e8aa0;
    --white: #ffffff;
  }
  * { box-sizing: border-box; margin: 0; padding: 0; }
  html, body {
    width: 1200px;
    height: 1200px;
    overflow: hidden;
    background: var(--backdrop);
  }
  .canvas {
    position: relative;
    width: 1200px;
    height: 1200px;
    display: flex;
    align-items: center;
    justify-content: center;
  }
  .lid {
    position: relative;
    width: 1000px;
    height: 934px;
    background: var(--paper);
    overflow: hidden;
    box-shadow: 0 10px 30px rgba(40, 60, 80, 0.15);
  }
  .brand {
    position: absolute;
    left: 300px;
    top: 150px;
    width: 260px;
    display: flex;
    flex-direction: column;
    align-items: center;
    gap: 14px;
  }
  .brand-mark {
    width: 40px;
    height: 40px;
    border: 4px solid var(--violet);
  }
  .brand-name {
    font-family: "Rubik", sans-serif;
    font-weight: 500;
    font-size: 26px;
    letter-spacing: 2px;
    text-transform: uppercase;
    color: var(--violet);
    white-space: nowrap;
  }
  .recipe-number {
    position: absolute;
    left: 300px;
    top: 275px;
    width: 260px;
    text-align: center;
    font-family: "Oswald", sans-serif;
    font-weight: 300;
    font-size: 54px;
    letter-spacing: 1px;
    color: var(--violet);
  }
  .lavender-field {
    position: absolute;
    left: 0;
    right: 0;
    top: 380px;
    height: 300px;
    background: linear-gradient(180deg, rgba(247,247,248,0) 0%, var(--lavender-light) 45%, var(--lavender-mid) 100%);
    clip-path: polygon(0 75%, 25% 55%, 45% 35%, 70% 10%, 100% 0, 100% 100%, 0 100%);
  }
  .name-band {
    position: absolute;
    left: 0;
    right: 0;
    top: 680px;
    height: 130px;
    background: var(--violet);
    display: flex;
    flex-direction: column;
    justify-content: center;
    align-items: flex-end;
    padding-right: 70px;
  }
  .product-name {
    font-family: "Rubik", sans-serif;
    font-weight: 300;
    font-size: 40px;
    line-height: 1.05;
    letter-spacing: 1px;
    color: var(--white);
    text-transform: uppercase;
    text-align: left;
  }
  .lavender-strip {
    position: absolute;
    left: 0;
    right: 0;
    top: 810px;
    bottom: 0;
    background: linear-gradient(180deg, var(--lavender-mid) 0%, var(--stem-grey) 100%);
  }
</style>
</head>
<body>
  <main class="canvas">
    <section class="lid">
      <div class="lavender-field" role="img" aria-label="Watercolour lavender sprigs rising across the lower lid"></div>

      <div class="brand">
        <span class="brand-mark"></span>
        <span class="brand-name">Harlow Soap Co.</span>
      </div>
      <h1 class="recipe-number">RECIPE NO. 6</h1>

      <div class="name-band">
        <p class="product-name">Lavender<br>+ Witch Hazel</p>
      </div>

      <div class="lavender-strip" role="img" aria-label="Band of lavender stems and leaves below the product name"></div>
    </section>
  </main>
</body>
</html>
```